Web Based Ordering. We have an existing input screen- Need to Clean it up

we have an existing ordering Modal on a trucking management system, but it looks and feels clunky. We would like to modernize the look and feel of it. We need to keep the same input fields, but we are open to any type of reconfiguration or layout changes you can think of to improve the flow and layout.

This design is for a web browser, not mobile app.

Target Market(s)

construction and trucking industry

Colors
85acd3
3176b5
33a6d7
85cae6
33b8a4
86cfc6

Requirements
Must have
• all the input fields displayed are required
Nice to have
• some of the fields can probably be combined to consolidate the number of tabs.

```html
<!DOCTYPE html>
<html lang="en">
<head>
<meta charset="utf-8">
<title>New Material Order</title>
<link rel="stylesheet" href="https://fonts.googleapis.com/css2?family=Poppins:wght@400;500;600;700&display=swap">
<style>
  :root {
    --page-bg: #a6d3e8;
    --header-start: #2a5aa6;
    --header-end: #2f93d2;
    --brand-blue: #2a5ea8;
    --toggle-blue: #1c64b8;
    --text-dark: #222629;
    --text-input: #35393d;
    --icon-grey: #6f7479;
    --border-input: #c8cdd3;
    --border-rule: #e2e5e9;
    --panel-bg: #ffffff;
  }
  * { box-sizing: border-box; margin: 0; padding: 0; }
  html, body { width: 1200px; height: 2697px; overflow: hidden; }
  body {
    background: var(--page-bg);
    font-family: "Poppins", sans-serif;
    color: var(--text-dark);
    position: relative;
  }
  .order-panel {
    position: absolute;
    left: 78px;
    width: 1044px;
    background: var(--panel-bg);
    box-shadow: 0 6px 22px rgba(40, 90, 140, 0.18);
  }
  .order-panel.step-destination { top: 90px; height: 993px; }
  .order-panel.step-date { top: 1139px; height: 705px; }
  .order-panel.step-material { top: 1902px; height: 705px; }

  .panel-header {
    height: 71px;
    background: linear-gradient(90deg, var(--header-start), var(--header-end));
    color: #fff;
    font-size: 24px;
    font-weight: 600;
    letter-spacing: 0.3px;
    text-align: center;
    line-height: 71px;
  }
  .step-tabs {
    height: 93px;
    border-bottom: 1px solid var(--border-rule);
    display: flex;
    justify-content: space-between;
    align-items: stretch;
    padding: 0 58px 0 45px;
    list-style: none;
  }
  .step-tab {
    display: flex;
    align-items: center;
    gap: 20px;
    font-size: 20px;
    font-weight: 500;
    color: var(--text-dark);
    position: relative;
  }
  .step-tab svg { width: 18px; height: 14px; flex: none; }
  .step-tab.is-active .tab-name { position: relative; height: 100%; display: flex; align-items: center; }
  .step-tab.is-active .tab-name::after {
    content: "";
    position: absolute;
    left: 1px; right: 1px; bottom: -1px;
    height: 3px;
    background: var(--brand-blue);
  }

  .panel-body { padding: 0 44px; }
  .field-row { display: grid; grid-template-columns: 475px 461px; column-gap: 20px; }
  .field-label {
    display: block;
    font-size: 15.5px;
    font-weight: 600;
    line-height: 20px;
    margin-bottom: 21px;
  }
  .field-label.caps { text-transform: uppercase; margin-bottom: 15px; }
  .input-box {
    height: 58px;
    border: 1px solid var(--border-input);
    border-radius: 2px;
    display: flex;
    align-items: center;
    padding: 0 22px;
    font-size: 15.5px;
    color: var(--text-input);
  }
  .input-box .value { flex: 1; white-space: nowrap; }
  .input-icons { display: flex; align-items: center; gap: 12px; color: var(--icon-grey); }
  .input-icons svg { display: block; }

  .outline-button {
    height: 48px;
    border: 2px solid var(--brand-blue);
    border-radius: 2px;
    background: #fff;
    color: var(--brand-blue);
    font-family: inherit;
    font-size: 15.5px;
    font-weight: 600;
    text-transform: uppercase;
    display: flex;
    align-items: center;
    justify-content: center;
    gap: 14px;
  }
  .add-button { width: 295px; }
  .form-actions { display: flex; justify-content: space-between; }
  .cancel-button { width: 162px; border-color: #2b2e31; color: #1d2023; }
  .continue-button { width: 163px; }

  .wage-toggle { display: flex; width: 195px; height: 49px; border: 2px solid var(--toggle-blue); border-radius: 2px; }
  .wage-toggle span {
    flex: 1;
    display: flex; align-items: center; justify-content: center;
    font-size: 15.5px; font-weight: 600; color: var(--toggle-blue);
  }
  .wage-toggle .opt-yes { flex: 0 0 92px; }
  .wage-toggle .is-selected { background: var(--toggle-blue); color: #fff; }
</style>
</head>
<body>

<svg width="0" height="0" style="position:absolute">
  <defs>
    <symbol id="icon-check" viewBox="0 0 18 14"><path d="M1.5 7.5 6.5 12 16.5 2" fill="none" stroke="#2a5ea8" stroke-width="3" stroke-linecap="round" stroke-linejoin="round"/></symbol>
    <symbol id="icon-clear" viewBox="0 0 12 12"><path d="M2 2 10 10 M10 2 2 10" stroke="currentColor" stroke-width="2.4" stroke-linecap="round"/></symbol>
    <symbol id="icon-caret" viewBox="0 0 12 7"><path d="M1 1h10L6 6z" fill="currentColor"/></symbol>
    <symbol id="icon-arrow" viewBox="0 0 16 14"><path d="M1 7h13M8.5 1.5 14 7l-5.5 5.5" fill="none" stroke="currentColor" stroke-width="2.4" stroke-linecap="round" stroke-linejoin="round"/></symbol>
  </defs>
</svg>

<!-- Destination step -->
<section class="order-panel step-destination">
  <h1 class="panel-header">NEW MATERIAL ORDER</h1>
  <ul class="step-tabs">
    <li class="step-tab"><svg><use href="#icon-check"/></svg><span class="tab-name">Date and Start</span></li>
    <li class="step-tab is-active"><svg><use href="#icon-check"/></svg><span class="tab-name">Destination</span></li>
    <li class="step-tab"><svg><use href="#icon-check"/></svg><span class="tab-name">Material</span></li>
    <li class="step-tab"><svg><use href="#icon-check"/></svg><span class="tab-name">Trucks</span></li>
    <li class="step-tab"><svg><use href="#icon-check"/></svg><span class="tab-name">Rates</span></li>
    <li class="step-tab"><svg><use href="#icon-check"/></svg><span class="tab-name">Summary</span></li>
  </ul>
  <div class="panel-body">
    <div class="field-row" style="margin-top:45px">
      <div><span class="field-label">PO /Job#</span>
        <div class="input-box"><span class="value">12</span><span class="input-icons"><svg width="12" height="12"><use href="#icon-clear"/></svg></span></div></div>
      <div><span class="field-label">Destination</span>
        <div class="input-box"><span class="value">RHC Plant 12- Millbrook</span><span class="input-icons"><svg width="12" height="12"><use href="#icon-clear"/></svg></span></div></div>
    </div>
    <div style="margin-top:17px"><span class="field-label">Address</span>
      <div class="input-box"><span class="value">4170 Harlan Industrial Parkway , Millbrook, GA, 30187</span></div></div>
    <div class="field-row" style="margin-top:26px">
      <div><span class="field-label">Job Site Contact</span>
        <div class="input-box"><span class="value">Derek Holloway</span><span class="input-icons"><svg width="12" height="12"><use href="#icon-clear"/></svg></span></div></div>
      <div><span class="field-label">Contact Number</span>
        <div class="input-box"><span class="value">(555) 014-2768</span><span class="input-icons"><svg width="12" height="12"><use href="#icon-clear"/></svg></span></div></div>
    </div>
    <button class="outline-button add-button" style="margin-top:27px">+ Add Second Destination</button>
    <div class="field-row" style="margin-top:28px">
      <div><span class="field-label">Billing Job Site</span>
        <div class="input-box"><span class="value">2109-Fairmont US 52/SR 7</span><span class="input-icons"><svg width="12" height="7"><use href="#icon-caret"/></svg></span></div></div>
      <div><span class="field-label">Phase Code</span>
        <div class="input-box"><span class="value">01. 0015., FIELD EN x</span><span class="input-icons"><svg width="12" height="7"><use href="#icon-caret"/></svg></span></div></div>
    </div>
    <div style="margin-top:28px"><span class="field-label caps">Prevailing Wage?</span>
      <div class="wage-toggle"><span class="opt-yes">YES</span><span class="is-selected">NO</span></div></div>
    <div class="form-actions" style="margin-top:38px">
      <button class="outline-button cancel-button">Cancel <svg width="16" height="14"><use href="#icon-arrow"/></svg></button>
      <button class="outline-button continue-button">Continue <svg width="16" height="14"><use href="#icon-arrow"/></svg></button>
    </div>
  </div>
</section>

<!-- Date and Start step -->
<section class="order-panel step-date">
  <h1 class="panel-header">NEW MATERIAL ORDER</h1>
  <ul class="step-tabs">
    <li class="step-tab is-active"><svg><use href="#icon-check"/></svg><span class="tab-name">Date and Start</span></li>
    <li class="step-tab"><svg><use href="#icon-check"/></svg><span class="tab-name">Destination</span></li>
    <li class="step-tab"><svg><use href="#icon-check"/></svg><span class="tab-name">Material</span></li>
    <li class="step-tab"><svg><use href="#icon-check"/></svg><span class="tab-name">Trucks</span></li>
    <li class="step-tab"><svg><use href="#icon-check"/></svg><span class="tab-name">Rates</span></li>
    <li class="step-tab"><svg><use href="#icon-check"/></svg><span class="tab-name">Summary</span></li>
  </ul>
  <div class="panel-body">
    <div style="margin-top:45px"><span class="field-label">Customer</span>
      <div class="input-box"><span class="value">R.H. Calloway Paving Company, Inc.</span><span class="input-icons"><svg width="12" height="12"><use href="#icon-clear"/></svg><svg width="12" height="7"><use href="#icon-caret"/></svg></span></div></div>
    <div style="margin-top:17px"><span class="field-label">Starting Location</span>
      <div class="input-box"><span class="value">2109-Fairmont US 52/SR 7</span><span class="input-icons"><svg width="12" height="12"><use href="#icon-clear"/></svg><svg width="12" height="7"><use href="#icon-caret"/></svg></span></div></div>
    <div class="field-row" style="margin-top:25px">
      <div><span class="field-label">Load Date</span>
        <div class="input-box"><span class="value">02/27/2021</span><span class="input-icons"><svg width="12" height="12"><use href="#icon-clear"/></svg></span></div></div>
      <div><span class="field-label">Load Time</span>
        <div class="input-box"><span class="value">6:00 AM</span><span class="input-icons"><svg width="12" height="12"><use href="#icon-clear"/></svg></span></div></div>
    </div>
    <div class="form-actions" style="margin-top:42px">
      <button class="outline-button cancel-button">Cancel <svg width="16" height="14"><use href="#icon-arrow"/></svg></button>
      <button class="outline-button continue-button">Continue <svg width="16" height="14"><use href="#icon-arrow"/></svg></button>
    </div>
  </div>
</section>

<!-- Material step -->
<section class="order-panel step-material">
  <h1 class="panel-header">NEW MATERIAL ORDER</h1>
  <ul class="step-tabs">
    <li class="step-tab"><svg><use href="#icon-check"/></svg><span class="tab-name">Date and Start</span></li>
    <li class="step-tab"><svg><use href="#icon-check"/></svg><span class="tab-name">Destination</span></li>
    <li class="step-tab is-active"><svg><use href="#icon-check"/></svg><span class="tab-name">Material</span></li>
    <li class="step-tab"><svg><use href="#icon-check"/></svg><span class="tab-name">Trucks</span></li>
    <li class="step-tab"><svg><use href="#icon-check"/></svg><span class="tab-name">Rates</span></li>
    <li class="step-tab"><svg><use href="#icon-check"/></svg><span class="tab-name">Summary</span></li>
  </ul>
  <div class="panel-body">
    <div style="margin-top:45px"><span class="field-label">Work Type</span>
      <div class="input-box"><span class="value">Asphalt — Machine Paving</span><span class="input-icons"><svg width="12" height="12"><use href="#icon-clear"/></svg><svg width="12" height="7"><use href="#icon-caret"/></svg></span></div></div>
    <div class="field-row" style="margin-top:17px">
      <div><span class="field-label">Material Type</span>
        <div class="input-box"><span class="value">12.5mm PEM</span><span class="input-icons"><svg width="12" height="12"><use href="#icon-clear"/></svg></span></div></div>
      <div><span class="field-label">Tonnage</span>
        <div class="input-box"><span class="value">400</span><span class="input-icons"><svg width="12" height="12"><use href="#icon-clear"/></svg></span></div></div>
    </div>
    <button class="outline-button add-button" style="margin-top:41px">+ Additional Material</button>
    <div class="form-actions" style="margin-top:46px">
      <button class="outline-button cancel-button">Cancel <svg width="16" height="14"><use href="#icon-arrow"/></svg></button>
      <button class="outline-button continue-button">Continue <svg width="16" height="14"><use href="#icon-arrow"/></svg></button>
    </div>
  </div>
</section>

</body>
</html>
```